Book cover - Quiet Rooms, Open Doors

Book cover for Ebook (Pagelight) and wrap around print cover (Printvale) (back, front, and spine)

The book title (may slightly change by end of brief):
(MAIN TITLE) 'Quiet Rooms, Open Doors'
(SUB HEADING) 'A Week-by-Week Practical Workbook to Loosen Nervous Habits, Quieten Doubt and Build Steady Poise'
by Dr Owen Hartley

I would like a bold, stand out cover. Contemporary. I would like to avoid stereotypical images of people looking anxious or worried. I would like the design to be more uplifting and hopeful, rather than focusing on the negative aspect of anxiety, but avoiding cliched photos of people raising their hands in the air, smiling and jumping etc. The cover should appeal to both men and women.

Trim size of book cover (for PrintVale) is 5.25" x 8" back and front with a spine size of 0.477 inches

Reason: I have decided to extend the deadline by 1 more day, not because I am unhappy with the quality of the designs, but because a few designers have contacted me to explain they have had technical difficulties when submitting their files. Thanks everyone for the hard work and great designs.

Target Market(s)

Males and females (16+) who struggle with social anxiety and shyness

Industry/Entity Type

Social

Font styles to use
Serif

Requirements
Must have
• Bold cover that is modern and contemporary. For example, I like these covers:
• http://shrtlnk.example/k4Tq9Zb
• http://shrtlnk.example/m8Wv2Hn
• http://shrtlnk.example/p3Jx6Lr
• http://shrtlnk.example/t7Gd1Qe
• http://shrtlnk.example/v2Nk8Fy
• http://shrtlnk.example/w9Bh4Cs
• http://shrtlnk.example/z5Mf3Ud
Nice to have
• Open to abstract designs.
Should not have
• No stereotypical pictures of people who look anxious or worried. Avoid cliched photos of people raising their hands in the air, smiling and jumping etc.

```html
<!DOCTYPE html>
<html lang="en">
<head>
<meta charset="utf-8">
<title>Quiet Rooms, Open Doors — Front Cover</title>
<link rel="stylesheet" href="https://fonts.googleapis.com/css2?family=Amatic+SC:wght@700&family=Special+Elite&display=swap">
<style>
  :root {
    --backdrop: #f1f1f1;
    --cover-black: #000000;
    --signal-yellow: #f5f10f;
    --accent-red: #e8140f;
    --ink: #111111;
    --paper-white: #ffffff;
  }
  * { margin: 0; padding: 0; box-sizing: border-box; }
  html, body {
    width: 1200px;
    height: 1200px;
    overflow: hidden;
    background: var(--backdrop);
  }
  .cover {
    position: absolute;
    left: 250px;
    top: 67px;
    width: 700px;
    height: 1066px;
    background: var(--cover-black);
    color: var(--paper-white);
  }
  .subtitle {
    position: absolute;
    top: 44px;
    left: 16px;
    right: 16px;
    font-family: "Amatic SC", "Arial Narrow", sans-serif;
    font-weight: 700;
    font-size: 28px;
    line-height: 1.25;
    letter-spacing: 2px;
    text-transform: uppercase;
    text-align: center;
  }
  .subtitle-line {
    display: block;
    white-space: nowrap;
  }
  .title {
    position: absolute;
    top: 140px;
    left: 0;
    right: 0;
    font-weight: normal;
  }
  .title-row {
    display: flex;
    justify-content: center;
    align-items: flex-end;
    height: 84px;
    margin-bottom: 4px;
  }
  .title-row--offset { margin-left: 24px; }
  .letter-disc {
    display: flex;
    align-items: center;
    justify-content: center;
    width: 88px;
    height: 84px;
    margin: 0 -3px;
    border-radius: 50%;
    background: var(--signal-yellow);
    color: var(--ink);
    font-family: "Special Elite", "Courier New", monospace;
    font-size: 66px;
    line-height: 1;
    text-transform: uppercase;
  }
  .letter-disc--accent { background: var(--accent-red); }
  .title-comma {
    color: var(--signal-yellow);
    font-family: "Special Elite", "Courier New", monospace;
    font-size: 66px;
    line-height: 0.9;
    margin-left: 6px;
  }
  .head-illustration {
    position: absolute;
    left: 215px;
    top: 556px;
    width: 262px;
    height: 350px;
    border-radius: 48% 46% 20% 30% / 40% 42% 20% 20%;
    background:
      radial-gradient(circle at 42% 36%, var(--signal-yellow) 0 19%, transparent 20%),
      radial-gradient(ellipse at 50% 45%, #4a4806 0%, #1b1a02 70%, #0a0a00 100%);
    border: 3px solid var(--signal-yellow);
  }
  .author {
    position: absolute;
    left: 0;
    right: 0;
    top: 945px;
    text-align: center;
    font-family: "Special Elite", "Courier New", monospace;
    font-size: 56px;
    letter-spacing: 1px;
    text-transform: uppercase;
    color: var(--paper-white);
    white-space: nowrap;
  }
</style>
</head>
<body>
  <main class="cover">
    <p class="subtitle">
      <span class="subtitle-line">A Week-by-Week Practical Workbook to Loosen Nervous</span>
      <span class="subtitle-line">Habits, Quieten Doubt and Build Steady Poise</span>
    </p>

    <h1 class="title" aria-label="Quiet Rooms, Open Doors">
      <span class="title-row" aria-hidden="true">
        <span class="letter-disc">Q</span><span class="letter-disc">U</span><span class="letter-disc">I</span><span class="letter-disc">E</span><span class="letter-disc">T</span>
      </span>
      <span class="title-row title-row--offset" aria-hidden="true">
        <span class="letter-disc">R</span><span class="letter-disc">O</span><span class="letter-disc">O</span><span class="letter-disc">M</span><span class="letter-disc">S</span><span class="title-comma">,</span>
      </span>
      <span class="title-row" aria-hidden="true">
        <span class="letter-disc">O</span><span class="letter-disc letter-disc--accent">P</span><span class="letter-disc">E</span><span class="letter-disc">N</span>
      </span>
      <span class="title-row" aria-hidden="true">
        <span class="letter-disc">D</span><span class="letter-disc">O</span><span class="letter-disc">O</span><span class="letter-disc">R</span><span class="letter-disc">S</span>
      </span>
    </h1>

    <div class="head-illustration" role="img" aria-label="Yellow line illustration of a head in profile, filled with a tangled web of lines around a bright yellow circle holding a small running figure"></div>

    <p class="author">Dr Owen Hartley</p>
  </main>
</body>
</html>
```